Business Card Design

Please see my website www.lqvesting.com.au to for further information on my services and styling of my site

Project Deadline Extended
Reason: Deadline is extended to permit alterations to current designs or for any new submissions. Cheers

Industry/Entity Type

Business

Contact Information for Business Card

Marcus Theale
Empowerment Coach

'Live your passion'

marcus@lqvcoaching.com.au
0437518264
lqvcoaching.com.au

```html
<!DOCTYPE html>
<html lang="en">
<head>
<meta charset="utf-8">
<title>LQV Coaching — Business Cards</title>
<link href="https://fonts.googleapis.com/css2?family=Open+Sans:wght@400;600;700&display=swap" rel="stylesheet">
<style>
  :root {
    --backdrop: #ffffff;
    --charcoal: #3b3b3c;
    --lime: #a6c83c;
    --swoosh-light: #e9e9e9;
    --swoosh-grey: #bdbdbd;
    --ink: #2a2a2a;
    --white: #ffffff;
  }
  * { margin: 0; padding: 0; box-sizing: border-box; }
  html, body {
    width: 1200px; height: 991px; overflow: hidden;
    background: var(--backdrop);
    font-family: "Open Sans", Arial, sans-serif;
  }
  .canvas { position: relative; width: 1200px; height: 991px; }

  .card {
    position: absolute;
    width: 600px; height: 366px;
    border-radius: 22px;
    overflow: hidden;
    box-shadow: 0 10px 28px rgba(0,0,0,0.22);
  }
  .card--back { left: 530px; top: 90px; background: var(--charcoal); }
  .card--front { left: 70px; top: 530px; }

  .card__bg { position: absolute; inset: 0; width: 100%; height: 100%; }

  .brand {
    position: absolute;
    display: flex; align-items: center; gap: 12px;
    color: var(--lime);
    font-weight: 700;
    line-height: 1.2;
    white-space: nowrap;
  }
  .brand__dot {
    width: 12px; height: 12px; border-radius: 50%;
    background: var(--lime);
  }
  .card--back .brand { left: 46px; top: 62px; font-size: 34px; }
  .card--front .brand { right: 40px; top: 72px; font-size: 36px; }

  .web-line {
    position: absolute; right: 42px; bottom: 70px;
    color: var(--white);
    font-size: 17px; letter-spacing: 3px;
  }
  .web-line__name { color: var(--lime); font-weight: 600; }

  .contact-list {
    position: absolute; left: 26px; top: 176px;
    list-style: none;
  }
  .contact-list li {
    display: flex; align-items: center; gap: 10px;
    color: var(--ink);
    font-size: 15px; line-height: 24px;
  }
  .contact-list svg { width: 16px; height: 16px; flex: none; }

  .person {
    position: absolute; right: 30px; bottom: 26px;
    text-align: right; color: var(--ink);
  }
  .person__name { font-size: 22px; font-weight: 700; }
  .person__role { font-size: 18px; font-weight: 400; margin-top: 2px; }
</style>
</head>
<body>
<main class="canvas">

  <section class="card card--back" aria-label="Card back">
    <div class="brand"><span class="brand__dot"></span>LQV Coaching</div>
    <p class="web-line">www.<span class="web-line__name">lqvcoaching</span>.com.au</p>
  </section>

  <section class="card card--front" aria-label="Card front">
    <svg class="card__bg" viewBox="0 0 600 366" preserveAspectRatio="none" aria-hidden="true">
      <rect width="600" height="366" fill="var(--lime)"/>
      <path d="M0 0 H600 V278 C420 218 200 158 0 143 Z" fill="var(--swoosh-grey)"/>
      <path d="M0 0 H600 V264 C420 204 200 144 0 129 Z" fill="var(--swoosh-light)"/>
      <path d="M0 0 H600 V250 C420 190 200 130 0 115 Z" fill="var(--charcoal)"/>
    </svg>

    <div class="brand"><span class="brand__dot"></span>LQV Coaching</div>

    <ul class="contact-list">
      <li>
        <svg viewBox="0 0 16 16" aria-hidden="true"><circle cx="8" cy="8" r="8" fill="var(--charcoal)"/><path d="M5.2 4.2l1.4-.3.8 1.8-.9.7c.4.9 1.1 1.6 2 2l.7-.9 1.8.8-.3 1.4c-3 .2-5.7-2.5-5.5-5.5z" fill="var(--white)"/></svg>
        0437518264
      </li>
      <li>
        <svg viewBox="0 0 16 16" aria-hidden="true"><circle cx="8" cy="8" r="8" fill="var(--charcoal)"/><rect x="4" y="5.2" width="8" height="5.6" fill="none" stroke="var(--white)" stroke-width="1"/><path d="M4 5.4l4 3 4-3" fill="none" stroke="var(--white)" stroke-width="1"/></svg>
        marcus@lqvcoaching.com.au
      </li>
      <li>
        <svg viewBox="0 0 16 16" aria-hidden="true"><circle cx="8" cy="8" r="8" fill="var(--charcoal)"/><circle cx="8" cy="8" r="4.2" fill="none" stroke="var(--white)" stroke-width="0.9"/><ellipse cx="8" cy="8" rx="1.8" ry="4.2" fill="none" stroke="var(--white)" stroke-width="0.9"/><path d="M3.8 8h8.4" stroke="var(--white)" stroke-width="0.9"/></svg>
        www.lqvcoaching.com.au
      </li>
    </ul>

    <div class="person">
      <p class="person__name">Marcus Theale</p>
      <p class="person__role">Empowerment Coach</p>
    </div>
  </section>

</main>
</body>
</html>
```